The Velvet Harbor Dancer

We have started working on a website for our short film. The goals of this website are:
• Attract talent, financiers + distributors to the feature film.
• Start e-commerce business to generate buzz for the film.

Who is our target audience?
• Kung Fu fans.
• Guitar players.
• Women filmmakers.
• Chinese film fans.

Information we want on this website.
Web 1.0 Components
• Media - trailer and stills

We are looking to include the following pages:
1. Home page
2. About
3. Photos
4. Cast & Crew
5. News
6. Media (reviews)
7. Store
8. Contact

Web 2.0 Components
• Mailing list sign-up
• Blog - with comments section
• Like / Add buttons - to all social networks
• Feeds - from social media
• Links - social media
• Widgets - that anyone can put on their sites

Attached is a mock up of the landing page (possible T-shirt) we are developing plus photos we would like on the website.

Thank you.

Reason: I am at a film market in meetings for my film project. Next week will be used for script rewrites. After that I will choose a design.

Hello Folks,

I have added my company logo to my brief. My answer is yes - I would like that added to the website.
Thanks!
R-

Reason: I have added more photos and included two (in front of a white screen) that can easily be photoshopped into a great landing page. R-

I have added more photos. Also I have two photos taken in front of a white screen that can easily be photo-shopped into a cool landing page. I have also gotten rid of the "crowd" photo in my mock up of the design I am looking for. 

I've extended the deadline by 2 days.

R-

Target Market(s)

• Kung Fu fans.
• Guitar players.
• Women filmmakers.
• Chinese film fans.

Industry/Entity Type

E-Commerce

Colors
ec2027

Requirements
Must have
• Trailer, movie stills, links to social media.
Nice to have
• All of the above

```html
<!DOCTYPE html>
<html lang="en">
<head>
<meta charset="utf-8">
<title>The Velvet Harbor Dancer</title>
<link rel="stylesheet" href="https://fonts.googleapis.com/css2?family=Lato:wght@400;700;900&display=swap">
<style>
  :root {
    --brand-red: #ec2027;
    --title-red: #d9303f;
    --title-grey: #d6d6d6;
    --ink: #1a1a1a;
    --body-ink: #2b2b2b;
    --panel-dark: #333333;
    --panel-line: #5a5a5a;
    --muted: #bdbdbd;
    --field: #f4f4f4;
    --white: #ffffff;
  }
  * { box-sizing: border-box; margin: 0; padding: 0; }
  html, body { width: 720px; height: 1200px; overflow: hidden; background: var(--white); }
  body { position: relative; font-family: "Lato", sans-serif; color: var(--ink); }

  .site-nav { position: absolute; top: 24px; left: 0; width: 720px; height: 16px; }
  .site-nav a { position: absolute; font-size: 11px; color: var(--ink); text-decoration: none; letter-spacing: 0.2px; }
  .site-nav a.is-current { color: var(--brand-red); font-weight: 700; }

  .hero-banner {
    position: absolute; left: 17px; top: 48px; width: 686px; height: 317px; overflow: hidden;
    background: radial-gradient(ellipse at 45% 40%, #b8223a 0%, #6e0c18 50%, #2a0508 100%);
  }
  .hero-still {
    position: absolute; left: 430px; top: 150px; width: 256px; height: 167px;
    background: radial-gradient(ellipse at 55% 60%, rgba(170,60,90,0.85) 0%, rgba(120,30,55,0.6) 45%, rgba(110,12,24,0) 75%);
  }
  .hero-title { position: absolute; left: 0; top: 0; width: 686px; height: 317px; text-transform: uppercase; }
  .hero-title span { position: absolute; white-space: nowrap; font-weight: 900; line-height: 1; }
  .hero-title .title-lead { left: 112px; top: 58px; font-size: 34px; color: var(--title-grey); }
  .hero-title .title-main { left: 48px; top: 98px; font-size: 58px; color: var(--title-red); letter-spacing: 1px; }
  .hero-title .title-tail { left: 168px; top: 162px; font-size: 44px; color: var(--title-grey); letter-spacing: 1px; }

  .main-article { position: absolute; left: 42px; top: 388px; width: 330px; }
  .main-article h1 { font-size: 14px; font-weight: 700; padding-bottom: 5px; border-bottom: 1.5px solid var(--brand-red); margin-bottom: 13px; }
  .main-article p { font-size: 9px; line-height: 12.8px; color: var(--body-ink); margin-bottom: 12.8px; }
  .main-article a.inline-link { display: block; font-size: 9px; line-height: 12.8px; font-weight: 700; color: var(--brand-red); text-decoration: none; margin-bottom: 12.8px; }

  .signup-field {
    position: absolute; left: 403px; top: 390px; width: 155px; height: 23px;
    border: 1px solid #cfcfcf; border-radius: 3px; background: var(--field);
    font-size: 6.5px; font-weight: 700; color: #555; padding: 8px 0 0 4px;
  }
  .social-links { position: absolute; left: 564px; top: 386px; width: 112px; height: 32px; display: flex; justify-content: space-between; }
  .social-link { width: 36px; display: flex; flex-direction: column; align-items: center; text-decoration: none; }
  .social-link .link-dot { width: 20px; height: 20px; border-radius: 50%; background: var(--brand-red); }
  .social-link .link-name { margin-top: 3px; font-size: 6.5px; font-weight: 700; color: var(--brand-red); white-space: nowrap; }

  .feed-panel { position: absolute; left: 403px; top: 436px; width: 270px; height: 324px; background: var(--panel-dark); border-radius: 6px; }
  .feed-title { position: absolute; left: 18px; top: 15px; font-size: 13px; color: var(--white); }
  .follow-button {
    position: absolute; left: 125px; top: 11px; width: 127px; height: 19px; background: #f2f2f2; border-radius: 3px;
    font-size: 6.3px; font-weight: 700; color: #444; padding: 6px 0 0 6px; white-space: nowrap; display: flex; gap: 4px;
  }
  .follow-button .button-dot { width: 7px; height: 7px; margin-top: -0.5px; border-radius: 50%; background: var(--brand-red); }
  .feed-rule { position: absolute; left: 18px; width: 234px; height: 1px; background: var(--panel-line); }
  .feed-item { position: absolute; left: 18px; width: 234px; height: 60px; }
  .feed-avatar { position: absolute; left: 0; top: 0; width: 57px; height: 57px; background: linear-gradient(160deg, #8a1a2a, #3a0c14); }
  .feed-name { position: absolute; left: 62px; top: 0; font-size: 11px; font-weight: 700; color: var(--white); }
  .feed-time { position: absolute; right: 4px; top: 1px; font-size: 9px; color: var(--muted); }
  .feed-text { position: absolute; left: 62px; top: 14px; font-size: 11px; color: #e6e6e6; }
  .feed-tag { position: absolute; left: 62px; top: 28px; font-size: 11px; color: var(--brand-red); }
  .feed-expand { position: absolute; left: 62px; top: 43px; font-size: 8.5px; color: var(--muted); }
  .reply-field { position: absolute; left: 18px; top: 287px; width: 234px; height: 20px; background: #cfcfcf; border-radius: 3px; font-size: 6.5px; font-weight: 700; color: #555; padding: 7px 0 0 3px; }

  .partner-panel { position: absolute; left: 403px; top: 783px; width: 270px; height: 314px; background: var(--brand-red); border-radius: 6px; }
  .partner-panel h2 { position: absolute; left: 20px; top: 19px; width: 223px; font-size: 13px; font-weight: 700; color: var(--white); padding-bottom: 7px; border-bottom: 1px solid #f58a8e; }
  .partner-card { position: absolute; left: 17px; top: 55px; width: 233px; height: 183px; background: var(--white); display: flex; align-items: center; justify-content: center; gap: 8px; }
  .partner-card .mark-dot { width: 20px; height: 20px; border-radius: 50%; background: var(--brand-red); flex: none; }
  .partner-card .partner-name { font-size: 18px; color: var(--brand-red); white-space: nowrap; }

  .site-footer { position: absolute; left: 17px; top: 1143px; width: 686px; border-top: 1px solid #f08a8d; }
  .site-footer p { position: absolute; left: 25px; top: 16px; font-size: 6px; color: var(--ink); white-space: nowrap; }
</style>
</head>
<body>
  <nav class="site-nav">
    <a class="is-current" style="left:42px">HOME</a>
    <a style="left:113px">ABOUT</a>
    <a style="left:190px">NEWS</a>
    <a style="left:272px">MEDIA</a>
    <a style="left:347px">PHOTOS</a>
    <a style="left:431px">CAST &amp; CREW</a>
    <a style="left:540px">STORE</a>
    <a style="left:614px">CONTACT</a>
  </nav>

  <header class="hero-banner">
    <div class="hero-still" role="img" aria-label="Still of the lead actress mid flying kick against a red starry backdrop"></div>
    <div class="hero-title">
      <span class="title-lead">The</span>
      <span class="title-main">Velvet Harbor</span>
      <span class="title-tail">Dancer</span>
    </div>
  </header>

  <article class="main-article">
    <h1>The Velvet Harbor Dancer</h1>
    <p>Text for home page Otatiis minctur? Quiae cum fuga. Ovid erument que alibusdae. Ut odi voluptatius, idundae. Et aliqui con nim id quas moditiam, odia delenem faccat iur, aped moluptate nis di cuptis nist reptas evelici toria vollent expelen dignis as quae corrorpor aut eos eum inulpa dolorehenit por si doluptur? Optatus mi, que sunt, que ne perum apiet vendis autest, sumenis accus dicti re nihitas eum, officipici iur, ut pratum quoste landenis experovit dita ipsam fuga. Rae et lantint andanti ducimusandes siti quae vendicimus.</p>
    <p>Inulla plaut enis il inum sumet autenis dus esectiat officto dolecum vel mi, in nus, qui diat quos earchil esciantiatur restrum fuga. Igenectatur, torehent.<br>Et quosam nos ereiciis eum eosa dolorerum nonem. Otam ipsa natem velent. Cius evere et audae possunt.</p>
    <a class="inline-link">Link can be inserted here</a>
    <p>Lautem. Itatio blaut ea dolenti auditatur? Qui totate re inciatquos sum et volutat que es moluptiamene reperferum, esedi untorpos aut quis eos rem vero ommolupta quaspe int accus mo tem que prest et ad molut es quidebit aut assinimi, sequia doluptin eriost poreici magnihi llignam, te endiam resequis aut assunt demquaes que niendenihil magnati orporiantes explit que rerum velignis coribus iusam vid molor onsero berferrum di accuptas dolori dolestem cor aborem. Remporunt ut et di quam id quo dolorep tiorepudit rem qui ut voluptatiam as nonem sam quo volupis dolut qui dolestiur seque porem quidebis ilic te etium ipis dolo tem. Ania pos con nos unt aut fugit, susaes dit am escil ipsantur?</p>
    <p>Udae nullabo rehendem re placera sitatiae molentor adis et arcimosam velenim olorepudis sunturisimpe ni optum aceseque dios voluptat esequistiae verspid magnienias am vel inctur sunt.</p>
    <a class="inline-link">Link can be inserted here</a>
    <p>Itiatiis de ario te sus, nimos ratum imagnitatem faceperum aut hil et doloria quas exernam ut atios velectaque arum, officiis et etur, sunduci tectiusam que modi consequibus dio molest et enda ant doluptas que arum quo iderion secuptaque velenimusdam nullabo. Accumquiate cuptassedit hictem sitisit atiam, sunt.<br>De et est que veles volupta et eaquam de exerum ab id quis volesto id mod quae volore mo quae nonsedi reperep eliquiatium volum ad quideni scipsae. Nam harchic ipsaperori ut landerum, tem. Neque doles peressim dolut et re nobis asped mos et autem. Natendion ea volor rate quo volores il et haribusame is expland escist iamenit atecumqui doleceptratus ex eumqui ducidus, sint, et molo blabo. Repeliquos expliqui as volor simus dioribea sitia quam, tem assed maxim fugitem im et harumquam faccum quodit, cum fugitate perecust quid qui reperep erunto volupta veni doluptati oditiorpori utem. Cid maioresti blat.<br>Otaqui dipsant, quas nam ipsus.</p>
    <p>Iia nonsequis sunt rem iume doloratur re pratem rehentotatur moluptas am volores cilisti unt as essumquo blabore ritatumquas diti dolorehendae consequo ex earcit re cum niententur? Ique volumqu iandit labo. Itaspe nos es apisquam estio enia sam, cuptasint auditat uscidistius.</p>
  </article>

  <div class="signup-field">Yes, send me news to my email address</div>
  <nav class="social-links">
    <a class="social-link"><span class="link-dot"></span><span class="link-name">Chirper</span></a>
    <a class="social-link"><span class="link-dot"></span><span class="link-name">Friendbook</span></a>
    <a class="social-link"><span class="link-dot"></span><span class="link-name">Feed</span></a>
  </nav>

  <section class="feed-panel">
    <div class="feed-title">Chirps</div>
    <div class="follow-button"><span class="button-dot"></span>Follow @TheVelvetHarborDancer</div>
    <div class="feed-rule" style="top:36px"></div>

    <div class="feed-item" style="top:55px">
      <div class="feed-avatar" role="img" aria-label="Profile photo of the lead actress"></div>
      <div class="feed-name">The Velvet Harbor Dancer</div><div class="feed-time">2min</div>
      <div class="feed-text">Chirper Feed News Goes here</div>
      <div class="feed-tag"># ChirperFeedTag</div>
      <div class="feed-expand">Expand</div>
    </div>
    <div class="feed-rule" style="top:124px"></div>

    <div class="feed-item" style="top:127px">
      <div class="feed-avatar" role="img" aria-label="Profile photo of the lead actress"></div>
      <div class="feed-name">The Velvet Harbor Dancer</div><div class="feed-time">2min</div>
      <div class="feed-text">Chirper Feed News Goes here</div>
      <div class="feed-tag"># ChirperFeedTag</div>
      <div class="feed-expand">Expand</div>
    </div>
    <div class="feed-rule" style="top:196px"></div>

    <div class="feed-item" style="top:199px">
      <div class="feed-avatar" role="img" aria-label="Profile photo of the lead actress"></div>
      <div class="feed-name">The Velvet Harbor Dancer</div><div class="feed-time">2min</div>
      <div class="feed-text">Chirper Feed News Goes here</div>
      <div class="feed-tag"># ChirperFeedTag</div>
      <div class="feed-expand">Expand</div>
    </div>
    <div class="feed-rule" style="top:268px"></div>

    <div class="reply-field">Chirp to @TheVelvetHarborDancer</div>
  </section>

  <section class="partner-panel">
    <h2>Production and Distribution</h2>
    <div class="partner-card">
      <span class="mark-dot"></span>
      <span class="partner-name">Lantern Bridge Films</span>
    </div>
  </section>

  <footer class="site-footer">
    <p>The Velvet Harbor Dancer is a Lantern Bridge Films production © 2014</p>
  </footer>
</body>
</html>
```